Bulk Food Container sticker

Our company sells bulk snacks to office locations. We re-package all sorts of foods into re-usable "Vessaline" type containers for consistency. We need to create a designed sticker which has room to laser-print the name of the food. The "blank" sticker needs to be designed with our logo, etc... I have attached 2 files. The first is an example from another company doing a similar work, and the second is the template from the company that will be printing the stickers for me. See our website for examples of our current corporate identity. www.brindlemoorbeans.com
Target Market(s)
Offices, tech companies
Industry/Entity Type
Printing
Look and feel

```html
<!DOCTYPE html>
<html lang="en">
<head>
<meta charset="utf-8">
<title>Brindlemoor container sticker sheet</title>
<link href="https://fonts.googleapis.com/css2?family=Nunito:wght@700;800;900&display=swap" rel="stylesheet">
<style>
  :root {
    --roast: #7f4500;
    --amber: #e06c00;
    --ink: #8a4a00;
    --edge: #2e1700;
    --paper: #ffffff;
  }
  html, body { margin: 0; padding: 0; }
  body {
    width: 928px; height: 1200px; overflow: hidden;
    background: var(--amber);
    font-family: "Nunito", "Verdana", sans-serif;
  }
  .sheet {
    position: relative;
    width: 1075px; height: 1390px;
    transform: scale(0.86326);
    transform-origin: 0 0;
    box-sizing: border-box;
    border: 2px solid var(--edge);
    background: linear-gradient(var(--roast) 0 1170px, var(--amber) 1170px 100%);
  }
  .label {
    position: absolute;
    width: 344px; height: 346px;
    box-sizing: border-box;
    border: 1.5px solid var(--edge);
    border-radius: 9px;
    overflow: hidden;
  }
  .label-tab {
    position: absolute;
    width: 344px; height: 30px;
    background: var(--amber);
    border-radius: 0 0 8px 8px;
  }
  .label-bg { position: absolute; inset: 0; width: 100%; height: 100%; }
  .brand {
    position: absolute; left: 0; right: 0; top: 22px;
    text-align: center;
    color: var(--paper);
    font-weight: 900; font-size: 38px; letter-spacing: 0.5px;
    line-height: 1;
  }
  .print-area {
    position: absolute; left: 22px; top: 89px;
    width: 302px; height: 217px;
    background: var(--paper);
    border-radius: 20px;
  }
  .slogan {
    position: absolute; left: 19px; bottom: 10px;
    color: var(--ink);
    font-weight: 800; font-size: 15.5px; line-height: 19px;
  }
  .slogan small {
    display: block;
    color: var(--amber);
    font-size: 10px; line-height: 11px; font-weight: 800;
  }
  .web {
    position: absolute; left: 0; right: 0; top: 312px;
    text-align: center;
    color: var(--paper);
    font-weight: 800; font-size: 17.5px; letter-spacing: 0.3px;
  }
  .mini {
    position: absolute;
    width: 172px; height: 63px;
    box-sizing: border-box;
    background: var(--amber);
    border: 1.5px solid var(--edge);
    border-radius: 8px;
  }
</style>
</head>
<body>
<div class="sheet">

  <!-- tabs under the first two rows -->
  <div class="label-tab" style="left:18px;top:396px"></div>
  <div class="label-tab" style="left:362px;top:396px"></div>
  <div class="label-tab" style="left:706px;top:396px"></div>
  <div class="label-tab" style="left:18px;top:774px"></div>
  <div class="label-tab" style="left:362px;top:774px"></div>
  <div class="label-tab" style="left:706px;top:774px"></div>

  <!-- row 1 -->
  <div class="label" style="left:18px;top:64px">
    <svg class="label-bg" viewBox="0 0 344 346" preserveAspectRatio="none"><rect width="344" height="346" fill="var(--roast)"/><polygon points="344,60 344,346 0,346 0,302" fill="var(--amber)"/></svg>
    <div class="brand">Brindlemoor</div>
    <div class="print-area"><div class="slogan">enhancing office<br>productivity...<small>one tub at a time</small></div></div>
    <div class="web">www.brindlemoorbeans.com</div>
  </div>
  <div class="label" style="left:362px;top:64px">
    <svg class="label-bg" viewBox="0 0 344 346" preserveAspectRatio="none"><rect width="344" height="346" fill="var(--roast)"/><polygon points="344,60 344,346 0,346 0,302" fill="var(--amber)"/></svg>
    <div class="brand">Brindlemoor</div>
    <div class="print-area"><div class="slogan">enhancing office<br>productivity...<small>one tub at a time</small></div></div>
    <div class="web">www.brindlemoorbeans.com</div>
  </div>
  <div class="label" style="left:706px;top:64px">
    <svg class="label-bg" viewBox="0 0 344 346" preserveAspectRatio="none"><rect width="344" height="346" fill="var(--roast)"/><polygon points="344,60 344,346 0,346 0,302" fill="var(--amber)"/></svg>
    <div class="brand">Brindlemoor</div>
    <div class="print-area"><div class="slogan">enhancing office<br>productivity...<small>one tub at a time</small></div></div>
    <div class="web">www.brindlemoorbeans.com</div>
  </div>

  <!-- row 2 -->
  <div class="label" style="left:18px;top:442px">
    <svg class="label-bg" viewBox="0 0 344 346" preserveAspectRatio="none"><rect width="344" height="346" fill="var(--roast)"/><polygon points="344,60 344,346 0,346 0,302" fill="var(--amber)"/></svg>
    <div class="brand">Brindlemoor</div>
    <div class="print-area"><div class="slogan">enhancing office<br>productivity...<small>one tub at a time</small></div></div>
    <div class="web">www.brindlemoorbeans.com</div>
  </div>
  <div class="label" style="left:362px;top:442px">
    <svg class="label-bg" viewBox="0 0 344 346" preserveAspectRatio="none"><rect width="344" height="346" fill="var(--roast)"/><polygon points="344,60 344,346 0,346 0,302" fill="var(--amber)"/></svg>
    <div class="brand">Brindlemoor</div>
    <div class="print-area"><div class="slogan">enhancing office<br>productivity...<small>one tub at a time</small></div></div>
    <div class="web">www.brindlemoorbeans.com</div>
  </div>
  <div class="label" style="left:706px;top:442px">
    <svg class="label-bg" viewBox="0 0 344 346" preserveAspectRatio="none"><rect width="344" height="346" fill="var(--roast)"/><polygon points="344,60 344,346 0,346 0,302" fill="var(--amber)"/></svg>
    <div class="brand">Brindlemoor</div>
    <div class="print-area"><div class="slogan">enhancing office<br>productivity...<small>one tub at a time</small></div></div>
    <div class="web">www.brindlemoorbeans.com</div>
  </div>

  <!-- row 3 -->
  <div class="label" style="left:18px;top:820px">
    <svg class="label-bg" viewBox="0 0 344 346" preserveAspectRatio="none"><rect width="344" height="346" fill="var(--roast)"/><polygon points="344,60 344,346 0,346 0,302" fill="var(--amber)"/></svg>
    <div class="brand">Brindlemoor</div>
    <div class="print-area"><div class="slogan">enhancing office<br>productivity...<small>one tub at a time</small></div></div>
    <div class="web">www.brindlemoorbeans.com</div>
  </div>
  <div class="label" style="left:362px;top:820px">
    <svg class="label-bg" viewBox="0 0 344 346" preserveAspectRatio="none"><rect width="344" height="346" fill="var(--roast)"/><polygon points="344,60 344,346 0,346 0,302" fill="var(--amber)"/></svg>
    <div class="brand">Brindlemoor</div>
    <div class="print-area"><div class="slogan">enhancing office<br>productivity...<small>one tub at a time</small></div></div>
    <div class="web">www.brindlemoorbeans.com</div>
  </div>
  <div class="label" style="left:706px;top:820px">
    <svg class="label-bg" viewBox="0 0 344 346" preserveAspectRatio="none"><rect width="344" height="346" fill="var(--roast)"/><polygon points="344,60 344,346 0,346 0,302" fill="var(--amber)"/></svg>
    <div class="brand">Brindlemoor</div>
    <div class="print-area"><div class="slogan">enhancing office<br>productivity...<small>one tub at a time</small></div></div>
    <div class="web">www.brindlemoorbeans.com</div>
  </div>

  <!-- small blank labels -->
  <div class="mini" style="left:18px;top:1185px"></div>
  <div class="mini" style="left:190px;top:1185px"></div>
  <div class="mini" style="left:362px;top:1185px"></div>
  <div class="mini" style="left:534px;top:1185px"></div>
  <div class="mini" style="left:706px;top:1185px"></div>
  <div class="mini" style="left:878px;top:1185px"></div>
  <div class="mini" style="left:18px;top:1264px"></div>
  <div class="mini" style="left:190px;top:1264px"></div>
  <div class="mini" style="left:362px;top:1264px"></div>
  <div class="mini" style="left:534px;top:1264px"></div>
  <div class="mini" style="left:706px;top:1264px"></div>
  <div class="mini" style="left:878px;top:1264px"></div>

</div>
</body>
</html>
```